依頼詳細
封筒サイズは角3と長3になります。主な郵送先は得意先への請求書の郵送、個人客へのパンフレットの郵送等が主な利用です。今使っている封筒はどこにでもある、ありきたりな物で
デザイン性が良いものを希望します。
記載項目
有限会社 葵岳照明工業
〒238-0417
神奈川県川崎市宮前区鷺沼8-7-4
TEL:044-912-3846
FAX:044-934-6718
Mail:info@aoitake-shomei.example.jp
希望イメージ
シンプル 複雑
単色 カラフル
暗い 明るい
日常 高級
遊び心 厳粛
未来的 伝統的
女性的 男性的
希望する色
黄・オレンジ系
納品ファイル
• 高解像度JPG (.jpg)
補足説明
ロゴマークと名刺のコピーを添付します
ロゴマークを入れてもらいたいと思います
名刺のデザインと色使いをリンクしたイメージを希望します
新たに添付ファイル追加します

```html
<!DOCTYPE html>
<html lang="ja">
<head>
<meta charset="utf-8">
<title>長3封筒 葵岳照明工業</title>
<link rel="stylesheet" href="https://fonts.googleapis.com/css2?family=Noto+Sans+JP:wght@400;500;700&family=Archivo+Black&display=swap">
<style>
  :root {
    --brand-orange: #e8772e;
    --ink: #2b2b2b;
    --paper: #ffffff;
  }
  * { margin: 0; padding: 0; box-sizing: border-box; }
  html, body {
    width: 1200px;
    height: 2620px;
    overflow: hidden;
    background: var(--paper);
  }
  .envelope {
    position: relative;
    width: 1200px;
    height: 2620px;
    background: var(--paper);
    font-family: "Noto Sans JP", sans-serif;
    color: var(--ink);
  }
  .flap-band {
    position: absolute;
    left: 0; top: 0;
    width: 1200px;
    height: 230px;
  }
  .postal-boxes {
    position: absolute;
    left: 662px;
    top: 376px;
    display: flex;
    align-items: center;
    gap: 6px;
  }
  .postal-box {
    width: 50px;
    height: 56px;
    border: 4px solid var(--brand-orange);
  }
  .postal-dash {
    width: 26px;
    height: 5px;
    margin: 0 4px;
    background: var(--brand-orange);
  }
  .sender {
    position: absolute;
    left: 296px;
    top: 1935px;
  }
  .sender-name {
    display: flex;
    align-items: center;
    gap: 22px;
    margin-left: 40px;
  }
  .sender-name .mark {
    width: 110px;
    height: 110px;
    border-radius: 50%;
    background: var(--brand-orange);
  }
  .sender-name .name {
    font-weight: 500;
    color: var(--ink);
    line-height: 1.15;
  }
  .sender-name .name-type { display: block; font-size: 34px; }
  .sender-name .name-main { display: block; font-size: 50px; letter-spacing: 1px; }
  .sender-address {
    margin-top: 30px;
    font-size: 33px;
    line-height: 44px;
    font-weight: 400;
  }
  .sender-address li {
    list-style: none;
    display: flex;
    align-items: center;
    gap: 8px;
  }
  .sender-address svg { width: 34px; height: 30px; flex: none; }
  .skyline {
    position: absolute;
    left: 292px;
    top: 2360px;
    width: 668px;
    height: 104px;
    background: linear-gradient(to bottom, rgba(232,119,46,0.55), var(--brand-orange));
  }
  .brand-band {
    position: absolute;
    left: 292px;
    top: 2462px;
    width: 668px;
    height: 80px;
    background: var(--brand-orange);
    display: flex;
    align-items: center;
    justify-content: center;
    font-family: "Archivo Black", sans-serif;
    font-size: 44px;
    color: var(--paper);
    letter-spacing: 1px;
  }
</style>
</head>
<body>
<main class="envelope">
  <svg class="flap-band" viewBox="0 0 1200 230" aria-hidden="true">
    <path d="M0 0H1200V162H728V48L600 210L472 48V162H0Z" fill="var(--brand-orange)"/>
    <path d="M490 30H710V96L600 224L490 96Z" fill="none" stroke="var(--paper)" stroke-width="0"/>
    <circle cx="600" cy="86" r="46" fill="var(--brand-orange)"/>
  </svg>

  <div class="postal-boxes" aria-label="郵便番号欄">
    <span class="postal-box"></span>
    <span class="postal-box"></span>
    <span class="postal-box"></span>
    <span class="postal-dash"></span>
    <span class="postal-box"></span>
    <span class="postal-box"></span>
    <span class="postal-box"></span>
    <span class="postal-box"></span>
  </div>

  <section class="sender">
    <div class="sender-name">
      <span class="mark"></span>
      <p class="name">
        <span class="name-type">有限会社</span>
        <span class="name-main">葵岳照明工業</span>
      </p>
    </div>
    <ul class="sender-address">
      <li>〒238-0417</li>
      <li>神奈川県川崎市宮前区鷺沼8-7-4</li>
      <li>
        <svg viewBox="0 0 34 30" aria-hidden="true"><path d="M4 10Q17 0 30 10L26 14L22 11V8Q17 6 12 8V11L8 14Z M7 16H27L30 28H4Z" fill="var(--ink)"/><circle cx="17" cy="21" r="3.5" fill="var(--paper)"/></svg>
        TEL 044-912-3846
      </li>
      <li>
        <svg viewBox="0 0 34 30" aria-hidden="true"><rect x="3" y="10" width="28" height="18" rx="2" fill="var(--ink)"/><rect x="8" y="2" width="18" height="10" fill="none" stroke="var(--ink)" stroke-width="2.5"/><rect x="8" y="15" width="18" height="3" fill="var(--paper)"/></svg>
        FAX 044-934-6718
      </li>
      <li>
        <svg viewBox="0 0 34 30" aria-hidden="true"><rect x="3" y="5" width="28" height="20" fill="none" stroke="var(--ink)" stroke-width="2.5"/><path d="M3 5L17 17L31 5" fill="none" stroke="var(--ink)" stroke-width="2.5"/></svg>
        MAIL info@aoitake-shomei.example.jp
      </li>
    </ul>
  </section>

  <div class="skyline" role="img" aria-label="オレンジ色の街並みのシルエット"></div>
  <div class="brand-band">AOITAKE-SHOMEI CO.,LTD</div>
</main>
</body>
</html>
```